Business card for Quorbital, LLC

I need a business card template in .ai or similar format for my IT consultancy, Quorbital(.com)

Front side: The usual name/title/number/fax/email/contact info. Definitely san-serif, the logo font is MuseoSans 500 so the company name (Quorbital, LLC.) should definitely be in the same type and the rest of the text should be that or something complimentary. Including logo on the front is optional - I would prefer designs that include both with and without. I am open to creative input on the format.

Back side: Company logo framed somehow. I was thinking red background with the logo in a white circle in the middle, tho' I'm not sure how that would play off the red ball in the elephant's trunk. Open to creative input here too.

Attached are a (very rough) one-sided card mock-up I made, along with the logo and logo font.

```html
<!DOCTYPE html>
<html lang="en">
<head>
<meta charset="utf-8">
<title>Quorbital, LLC — Business Card</title>
<link href="https://fonts.googleapis.com/css2?family=Nunito+Sans:wght@400;600;800&display=swap" rel="stylesheet">
<style>
  :root {
    --stage: #e4e4e4;
    --card-dark: #434343;
    --card-light: #ffffff;
    --brand-red: #e8202e;
    --ink: #222222;
    --ink-soft: #777777;
    --on-dark: #e9e9e9;
  }
  * { box-sizing: border-box; margin: 0; padding: 0; }
  html, body {
    width: 1200px;
    height: 748px;
    overflow: hidden;
  }
  body {
    background: var(--stage);
    font-family: "Nunito Sans", Arial, sans-serif;
    display: flex;
    align-items: center;
    justify-content: center;
    gap: 64px;
  }
  .card {
    width: 340px;
    height: 340px;
    border-radius: 18px;
    position: relative;
    box-shadow: 0 6px 18px rgba(0,0,0,0.18);
  }

  /* Back side */
  .card--back {
    background: var(--card-dark);
    display: flex;
    flex-direction: column;
    align-items: center;
  }
  .card--back .brand-mark {
    margin-top: 108px;
    display: flex;
    align-items: center;
    gap: 12px;
  }
  .brand-dot {
    width: 26px;
    height: 26px;
    border-radius: 50%;
    background: var(--brand-red);
  }
  .brand-name {
    font-weight: 800;
    font-size: 40px;
    letter-spacing: 0.5px;
    color: var(--brand-red);
    line-height: 1;
  }
  .card--back .website {
    position: absolute;
    bottom: 26px;
    width: 100%;
    text-align: center;
    font-size: 11px;
    color: var(--on-dark);
    letter-spacing: 0.3px;
  }

  /* Front side */
  .card--front {
    background: var(--card-light);
    color: var(--ink);
  }
  .card--front .brand-mark {
    position: absolute;
    top: 58px;
    right: 26px;
    display: flex;
    align-items: center;
    gap: 7px;
  }
  .card--front .brand-dot {
    width: 14px;
    height: 14px;
    background: var(--card-dark);
  }
  .card--front .brand-name {
    font-size: 18px;
  }
  .identity {
    position: absolute;
    top: 152px;
    width: 100%;
    text-align: center;
  }
  .person-name {
    font-weight: 400;
    font-size: 20px;
    color: var(--ink);
  }
  .person-title {
    font-size: 12px;
    color: var(--ink-soft);
    margin-top: 1px;
  }
  .contact {
    position: absolute;
    top: 250px;
    width: 100%;
    text-align: center;
    font-size: 11.5px;
    line-height: 15px;
    list-style: none;
  }
  .contact .label { color: var(--brand-red); }
  .contact .address { font-size: 12px; color: var(--ink); }
</style>
</head>
<body>

  <section class="card card--back" aria-label="Card back">
    <div class="brand-mark">
      <span class="brand-dot"></span>
      <span class="brand-name">QUORBITAL</span>
    </div>
    <p class="website">www.quorbital.com</p>
  </section>

  <section class="card card--front" aria-label="Card front">
    <div class="brand-mark">
      <span class="brand-dot"></span>
      <span class="brand-name">QUORBITAL</span>
    </div>
    <div class="identity">
      <h1 class="person-name">Dana Petrov</h1>
      <p class="person-title">Problem Eliminator</p>
    </div>
    <ul class="contact">
      <li class="address">12 Larkspur Ct. Fern Hollow, PA 19000-2160</li>
      <li><span class="label">Email:</span> dpetrov@quorbital.com</li>
      <li><span class="label">Phone:</span> 1.800.555.0142</li>
      <li><span class="label">Mobile:</span> 1.215.555.0187</li>
      <li><span class="label">Fax:</span> 1.215.555.0163</li>
    </ul>
  </section>

</body>
</html>
```